" Ela ainda não está funcionando, mas a ideia é ser uma loja virtual com todas as informações e facilidades para locação de cadeirinhas infantis, carrinhos, tapetinhos, brinquedos, cadeiras de automóveis, etc. Todos os itens serão entregues e recolhidos nos endereços informados pelos clientes. A principal ideia é facilitar a vida das mães que viajam com crianças pequenas. É sempre muito trabalhoso carregar toda a tralha infantil, portanto facilitaremos a vida locando todos os equipamentos no destino, entregando e recolhendo em qualquer localidade de Vila Aurora. Praticidade, facilidade e comodidade para as mães que precisem de itens essenciais para o dia a dia dos bebês. "

```html
<!DOCTYPE html>
<html lang="pt-BR">
<head>
<meta charset="UTF-8">
<title>Pequeno Viajante – Chegou</title>
<link rel="stylesheet" href="https://fonts.googleapis.com/css2?family=Baloo+2:wght@600;700;800&family=Open+Sans:wght@400;600;700&display=swap">
<style>
  :root {
    --page-bg: #eef1f2;
    --flyer-bg: #def1f5;
    --flyer-bg-deep: #cfe8ef;
    --teal-dark: #235f70;
    --teal: #2f7d90;
    --sky: #5cb9d8;
    --band: #cbe7ee;
    --orange: #f4a21c;
    --ink: #3c4a50;
    --card: #ffffff;
    --cloud: #ffffff;
  }
  * { margin: 0; padding: 0; box-sizing: border-box; }
  html, body {
    width: 1200px; height: 1200px; overflow: hidden;
    background: var(--page-bg);
    font-family: "Open Sans", Arial, sans-serif;
  }
  .flyer {
    position: absolute; left: 210px; top: 45px;
    width: 780px; height: 1110px;
    background: linear-gradient(180deg, var(--flyer-bg) 0%, #e6f5f8 55%, var(--flyer-bg-deep) 100%);
    overflow: hidden;
    box-shadow: 0 6px 24px rgba(0,0,0,.12);
  }
  .cloud {
    position: absolute; left: 50px; top: 52px; width: 373px; height: 160px;
    border-radius: 80px;
    background: radial-gradient(ellipse at 50% 40%, var(--cloud) 55%, #e9f4f7 100%);
  }
  .headline {
    position: absolute; left: 50px; top: 82px; width: 373px;
    text-align: center;
    font-family: "Baloo 2", "Comic Sans MS", sans-serif;
    font-weight: 700; font-size: 54px; line-height: 1;
    color: var(--orange);
  }
  .brand-lockup {
    position: absolute; left: 393px; top: 178px;
    display: flex; align-items: center; gap: 10px;
  }
  .brand-name {
    font-family: "Baloo 2", "Comic Sans MS", sans-serif;
    font-weight: 800; font-size: 44px; line-height: .95;
    color: var(--orange);
  }
  .brand-mark {
    width: 14px; height: 14px; border-radius: 50%; background: var(--orange);
  }
  .plane-art {
    position: absolute; left: 630px; top: 184px; width: 104px; height: 96px;
    border-radius: 10px;
    background: linear-gradient(135deg, #f7c46a, var(--orange) 60%, var(--teal));
  }
  .flight-path { position: absolute; left: 560px; top: 262px; }
  .stroller-art {
    position: absolute; left: 70px; top: 324px; width: 300px; height: 340px;
    border-radius: 40px;
    background: linear-gradient(180deg, #f3dcc6 0%, #bfe3ef 40%, var(--sky) 100%);
  }
  .info-tag {
    position: absolute; left: 380px; top: 366px; width: 328px; height: 266px;
    background: var(--card);
    border: 3px solid #cfdadd;
    border-radius: 8px;
    transform: rotate(-2deg);
    padding: 38px 26px 20px 26px;
    box-shadow: 0 3px 8px rgba(0,0,0,.08);
  }
  .info-tag::before {
    content: ""; position: absolute; inset: 8px;
    border: 2px dashed #b9cdd2; border-radius: 5px;
  }
  .tag-hole {
    position: absolute; right: 22px; top: 12px; width: 18px; height: 18px;
    border-radius: 50%; border: 3px solid #b9cdd2; background: var(--flyer-bg);
  }
  .tag-text {
    position: relative; font-size: 13px; line-height: 1.45; color: var(--ink);
  }
  .tag-text + .tag-text { margin-top: 14px; }
  .tag-text .accent { color: var(--orange); font-weight: 600; }
  .cta-band {
    position: absolute; left: 8px; top: 676px; width: 764px; height: 84px;
    background: var(--band);
    border: 3px dashed var(--teal);
    display: flex; align-items: center; justify-content: center;
  }
  .cta-text {
    font-weight: 700; font-size: 40px; letter-spacing: .5px; color: var(--teal-dark);
  }
  .brand-lockup-small {
    position: absolute; left: 290px; top: 786px;
    display: flex; align-items: center; gap: 8px;
  }
  .brand-lockup-small .brand-name { font-size: 26px; }
  .brand-lockup-small .brand-mark { width: 9px; height: 9px; }
  .plane-art-small {
    position: absolute; left: 430px; top: 788px; width: 78px; height: 62px;
    border-radius: 8px;
    background: linear-gradient(135deg, #f7c46a, var(--orange) 60%, var(--teal));
  }
  .promise-box {
    position: absolute; left: 168px; top: 886px; width: 486px; height: 88px;
    background: var(--teal-dark);
    display: flex; align-items: center; justify-content: center;
    padding: 0 18px; text-align: center;
  }
  .promise-text { color: #e8f6f9; font-size: 18px; line-height: 1.3; }
  .promise-curl { position: absolute; left: 650px; top: 870px; }
  .website {
    position: absolute; left: 0; top: 1036px; width: 780px; text-align: center;
    font-weight: 700; font-size: 26px; color: var(--teal-dark);
  }
</style>
</head>
<body>
  <main class="flyer">
    <div class="cloud" role="img" aria-label="Ilustração de nuvem branca"></div>
    <h1 class="headline">Chegou</h1>

    <div class="brand-lockup">
      <span class="brand-name">Pequeno<br>Viajante</span>
      <span class="brand-mark"></span>
    </div>
    <div class="plane-art" role="img" aria-label="Ilustração de avião de papel"></div>
    <svg class="flight-path" width="90" height="100" viewBox="0 0 90 100">
      <path d="M80 8 C 60 40, 75 70, 45 62 S 10 80, 5 98" fill="none" stroke="#3c4a50" stroke-width="2.5" stroke-dasharray="6 6"/>
    </svg>

    <div class="stroller-art" role="img" aria-label="Ilustração de bebê com chupeta em um carrinho azul"></div>

    <div class="info-tag">
      <span class="tag-hole"></span>
      <p class="tag-text">Facilitando a vida das famílias que viajam com crianças pequenas, locando todos os equipamentos no destino, entregando e recolhendo em qualquer localidade de <span class="accent">Vila Aurora</span>.</p>
      <p class="tag-text">Planeje sua viagem com leveza, reserve os itens pelo site e deixe a bagagem pesada para trás.</p>
    </div>

    <div class="cta-band"><p class="cta-text">VENHA CONFERIR!</p></div>

    <div class="brand-lockup-small">
      <span class="brand-name">Pequeno<br>Viajante</span>
      <span class="brand-mark"></span>
    </div>
    <div class="plane-art-small" role="img" aria-label="Ilustração de avião de papel"></div>

    <div class="promise-box">
      <p class="promise-text">Praticidade, facilidade e comodidade para as mães que precisem de itens essenciais para o dia a dia dos bebês.</p>
    </div>
    <svg class="promise-curl" width="90" height="80" viewBox="0 0 90 80">
      <path d="M5 55 C 30 60, 40 30, 60 28 S 85 45, 70 60" fill="none" stroke="#3c4a50" stroke-width="2.5" stroke-dasharray="6 6"/>
    </svg>

    <p class="website">www.pequenoviajante.com.br</p>
  </main>
</body>
</html>
```